2 Page Business Flyer for Finance Business

Need a two page flyer created for a finance business. Lots of text and needs to fit on two pages.

Corporate business/banking look and feel. Not too many large images. Lots of white space, clean design. Attached is color palette and the text contents of the flyer.

```html
<!DOCTYPE html>
<html lang="en">
<head>
<meta charset="utf-8">
<title>Vanilla Options – Two Page Flyer</title>
<link rel="stylesheet" href="https://fonts.googleapis.com/css2?family=Oswald:wght@500;600;700&family=Roboto:wght@400;500&family=Lato:ital,wght@0,400;0,700;0,900;1,400;1,700&display=swap">
<style>
:root{
  --teal:#3ccab4;
  --teal-deep:#26a996;
  --ink:#2b2b2b;
  --charcoal:#353535;
  --charcoal-soft:#444;
  --paper:#ffffff;
  --board:#e4e4e4;
  --muted:#cfcfcf;
}
*{box-sizing:border-box;margin:0;padding:0}
html,body{width:1200px;height:902px;overflow:hidden}
body{background:var(--board);position:relative;font-family:"Lato",Arial,sans-serif;color:var(--ink)}
.page{position:absolute;width:511px;height:718px;background:var(--paper);overflow:hidden;transform:scale(.97);transform-origin:top left}
.page--front{left:86px;top:128px}
.page--back{left:658px;top:46px}
.abs{position:absolute}
.bar-top{left:0;top:0;width:100%;height:23px;background:var(--charcoal)}
.bar-bottom{left:0;bottom:0;width:100%;height:26px;background:var(--teal)}
p.body{font-size:7.4px;line-height:9.4px;text-align:justify;color:#333}
p.body + p.body{margin-top:6px}

/* FRONT */
.hero{left:0;top:23px;width:511px;height:283px;background:linear-gradient(90deg,#6b8fa8 0%,#9fb9c9 30%,#8fd9cc 55%,#4fcdb8 80%,#3ccab4 100%)}
.hero-title{left:225px;top:42px;font-family:"Oswald",sans-serif;color:var(--ink);text-transform:uppercase;line-height:1}
.hero-title .small{display:block;font-size:21px;font-weight:600;letter-spacing:.3px}
.hero-title .big{display:block;font-size:32px;font-weight:700;margin-top:9px;letter-spacing:.5px}
.hero-copy{left:170px;top:122px;width:322px}
.steps{left:228px;top:228px;list-style:none}
.steps li{font-size:7.4px;font-weight:700;font-style:italic;color:#1f1f1f;margin-bottom:7.5px;position:relative;padding-left:18px}
.steps li::before{content:"";position:absolute;left:0;top:1px;width:7px;height:7px;border-radius:50%;background:#fff}
.side-stub{left:0;top:306px;width:32px;height:228px;background:var(--teal)}
.banner{height:38px;background:var(--charcoal)}
.banner span{position:absolute;left:12px;top:5px;font-family:"Roboto",sans-serif;font-size:22px;color:#fff;letter-spacing:.3px;white-space:nowrap}
.banner-example{left:30px;top:308px;width:410px;clip-path:polygon(0 0,100% 0,93% 100%,0 100%)}
.example-head{left:44px;top:353px;font-family:"Roboto",sans-serif;font-size:17px;color:var(--teal);letter-spacing:.2px}
.col-a{left:44px;top:379px;width:222px}
.col-b{left:273px;top:355px;width:220px}
.info{left:0;top:538px;width:511px;height:155px;background:linear-gradient(180deg,#3a3a3a,#2e2e2e)}
.tab{top:12px;height:24px;background:#242424;clip-path:polygon(0 0,92% 0,100% 50%,92% 100%,0 100%,6% 50%);font-family:"Lato",sans-serif;font-weight:700;font-size:12px;color:var(--teal);text-align:center;line-height:24px;letter-spacing:.3px}
.tab-char{left:22px;width:150px}
.tab-adv{left:180px;width:140px}
.tab-risk{left:340px;width:150px}
.ticks{list-style:none;top:48px}
.ticks li{font-size:6.7px;line-height:8.4px;font-weight:700;font-style:italic;color:#eee;position:relative;padding-left:13px;margin-bottom:9px}
.ticks li::before{content:"";position:absolute;left:0;top:1px;width:5.5px;height:5.5px;border-radius:50%;background:var(--teal)}
.ticks-char{left:16px;width:160px}
.ticks-adv{left:188px;width:150px}
.ticks-risk{left:357px;width:120px}

/* BACK */
.back-top{left:0;top:23px;width:511px;height:283px;background:var(--teal)}
.portrait{left:0;top:23px;width:250px;height:283px;background:linear-gradient(180deg,#48cdb8 0%,#3a4250 55%,#22262d 100%)}
.why-title{left:282px;top:44px;font-family:"Oswald",sans-serif;text-transform:uppercase;line-height:1}
.why-title .big{display:block;font-size:60px;font-weight:700;color:#fff;letter-spacing:.5px}
.why-title .small{display:block;font-size:29px;font-weight:600;color:var(--ink);margin-top:6px}
.why-copy{left:279px;top:158px;width:204px}
.why-copy p{font-size:9.2px;line-height:11.1px;font-weight:700;text-align:justify;color:#1f2a28}
.stub-back{left:0;top:311px;width:40px;height:243px;background:var(--teal)}
.banner-price{left:40px;top:312px;width:388px;height:72px;clip-path:polygon(0 0,100% 0,84% 100%,0 100%)}
.banner-price span{top:10px;font-size:20.5px;line-height:26px}
.money{left:308px;top:345px;width:180px;height:175px;background:radial-gradient(ellipse at 55% 60%,#c9d2c4 0%,#e3e8df 55%,#ffffff 80%)}
.price-copy{left:57px;top:395px;width:242px}
.price-copy p{font-size:8.3px;line-height:10px;color:#333;text-align:justify}
.vars-head{left:55px;top:448px;width:240px;font-size:12px;font-weight:700;line-height:15px;color:#222}
.vars{left:56px;top:489px;list-style:none;width:440px}
.vars li{font-size:7.7px;font-style:italic;font-weight:700;color:#1f1f1f;position:relative;padding-left:16px;margin-bottom:6.6px}
.vars li::before{content:"";position:absolute;left:0;top:1px;width:7px;height:7px;border-radius:50%;background:var(--teal)}
.note{left:0;top:601px;width:511px;height:92px;background:linear-gradient(180deg,#2f2f2f,#3a3a3a)}
.note p{position:absolute;left:46px;top:20px;width:450px;font-size:8.6px;line-height:11.2px;font-style:italic;font-weight:700;color:#f2f2f2;text-align:justify}
</style>
</head>
<body>

<section class="page page--front" aria-label="Front page">
  <div class="abs bar-top"></div>
  <div class="abs hero" role="img" aria-label="Photograph of two businessmen shaking hands in front of glass office towers, blending into teal"></div>
  <h1 class="abs hero-title"><span class="small">How does a vanilla option</span><span class="big">Contract work?</span></h1>
  <div class="abs hero-copy">
    <p class="body">The buyer of a vanilla option receives protection against an adverse movement in the exchange rate while allowing full participation in a beneficial move. At no time is the buyer of a Vanilla Option obligated to exercise the Option and transact the currencies, therefore providing flexibility in cases where the requirement to purchase foreign currency is not certain.</p>
    <p class="body">A buyer of vanilla options is required to pay a premium (like an insurance premium) for the right, but not the obligation, to exchange currency at a predetermined rate on a predetermined date.</p>
  </div>
  <ul class="abs steps">
    <li>Set a protection rate which will be your worst-case scenario at expiry</li>
    <li>Determine the amount of currency you wish to protect</li>
    <li>Choose an expiry date for the contract</li>
    <li>Calculate the premium you are required to pay</li>
  </ul>

  <div class="abs side-stub"></div>
  <div class="abs banner banner-example"><span>LET’S LOOK AT AN EXAMPLE:</span></div>
  <h2 class="abs example-head">YOU ARE IN IMPORTER.</h2>
  <div class="abs col-a">
    <p class="body">Your construction company has bid on a project that if successful, will require you to import materials from the United States to use in construction. You have used todays pricing of materials in calculating your bid and want to protect against an adverse move in the US dollar exchange rate from eroding your margin if your bid is chosen for the project.</p>
    <p class="body">You choose to buy a Vanilla Call which will protect you from a rise in the USD/CAD exchange rate above your protection rate. You choose to buy protection on $500,000 USD, with a protection rate (strike rate) of 1.3300 expiring 3 months from now. You are required to pay a premium which in this case is calculated to be 1.8%, or 11,970 CAD.</p>
  </div>
  <div class="abs col-b">
    <p class="body">Your bid is successful: If the exchange rate is below your protection rate at expiration, you have no obligation relating to the vanilla call and you are free to buy USD at the cheaper spot rate. If the exchange rate is above your protection rate, your have the right to purchase your USD at the protection rate, and thereby claiming your insurance policy.</p>
    <p class="body">Your bid is not successful: You have no obligation relating to the vanilla option however, if at expiry the exchange rate is above the protection rate, you may exercise your right to buy USD at the lower rate and simultaneous sell USD back at the prevailing spot rate, thereby recouping some or all of the premium paid to buy the option. Alternatively, if you find out your bid was not successful with time still left until expiration, you may sell your option back into the market in the case that it still has residual value, which will depend on various market factors.</p>
  </div>

  <div class="abs info">
    <div class="abs tab tab-char">CHARACTERISTICS</div>
    <div class="abs tab tab-adv">ADVANTAGES</div>
    <div class="abs tab tab-risk">RISKS</div>
    <ul class="abs ticks ticks-char">
      <li>You are looking for a straight-forward hedging solution</li>
      <li>You want to receive full benefit from an appreciation of the currency you are exposed to</li>
      <li>You are comfortable receiving protection at the strike rate of the option</li>
      <li>You are willing to pay the non-refundable premium</li>
    </ul>
    <ul class="abs ticks ticks-adv">
      <li>You hedge your foreign currency exposure at a predefined hedge rate</li>
      <li>You can choose the hedge rate that suits your budget requirements</li>
      <li>Provides the ability to fully participate in a favourable exchange rate move</li>
      <li>You can choose from most major currency pairs to meet your needs</li>
    </ul>
    <ul class="abs ticks ticks-risk">
      <li>Premium paid is non-refundable and remains your only obligation when buying vanilla options</li>
    </ul>
  </div>
  <div class="abs bar-bottom"></div>
</section>

<section class="page page--back" aria-label="Back page">
  <div class="abs bar-top"></div>
  <div class="abs back-top"></div>
  <div class="abs portrait" role="img" aria-label="Photograph of a smiling businesswoman in a dark suit holding a blue folder and gesturing towards the heading"></div>
  <h1 class="abs why-title"><span class="big">Why use</span><span class="small">Vanilla options?</span></h1>
  <div class="abs why-copy">
    <p>Vanilla options are often compared to an insurance product. The buyer pays a non-refundable premium for the right, but not the obligation to trade currency in the future at the protection rate of the option. This product allows you to participate in a beneficial move to an unlimited extent, which will be the most advantageous outcome, if the exchange rate moves in your favour enough to more than offset the premium paid for the option.</p>
  </div>

  <div class="abs stub-back"></div>
  <div class="abs banner banner-price"><span class="abs">WHAT DETERMINES THE PRICE<br>OF A VANILLA OPTION?</span></div>
  <div class="abs money" role="img" aria-label="Illustration of rising stacks of banknotes with a gold arrow climbing upward"></div>
  <div class="abs price-copy">
    <p>The cost of an option is defined by the premium that is required to be paid in order to enter into the contract. Premiums are calculated using the industry standard formulas based upon the Black Scholes model.</p>
  </div>
  <h2 class="abs vars-head">The most important variables in the option pricing formulas include the following:</h2>
  <ul class="abs vars">
    <li>The current market Spot Rate.</li>
    <li>Market volatility – the higher the volatility, the higher the premium.</li>
    <li>The Term of the Option – a longer term typically results in a higher premium.</li>
    <li>The Strike Rate – the closer to being ITM the protection rate is, the higher the premium.</li>
    <li>The interest rate differential of the two currencies involved.</li>
    <li>Style – European or American, or whether the option can be exercised prior to expiration</li>
  </ul>

  <div class="abs note">
    <p>An option can either a European (meaning that they can only be exercised on the expiry date), or American (meaning that they can be exercised at any time prior to expiration). We normally deals in European options however, we do offer American options under certain circumstances and when specific delivery terms are agreed upon between us and the customer.</p>
  </div>
  <div class="abs bar-bottom"></div>
</section>

</body>
</html>
```